Hip and quirky Indian restaurant Menu

We need a build your own bowl/meal/wrap menu similar to Verdigo others. We would like illustrations if possible of India/veggies/chicken/animals/themes. Please utilize the colors that match the schema of the logos provided. We have included pictures you may use them if you would like to. Menu provided is our old menu.

Target Market(s)

Millenials, Ge

Industry/Entity Type

Retail

Font styles to use
Sans Serif
Decorative

Requirements
Must have
• logical placements for build your own meal options
Nice to have
• Illustrations.

```html
<!DOCTYPE html>
<html lang="en">
<head>
<meta charset="utf-8">
<title>Tadka Lane Menu</title>
<link href="https://fonts.googleapis.com/css2?family=Montserrat:wght@500;600;700;800&display=swap" rel="stylesheet">
<style>
:root{
  --stage:#424242;
  --navy:#262262;
  --red:#ed1c24;
  --magenta:#9e1f63;
  --orange:#f26a36;
  --cream:#fddca3;
  --ink:#4a1f4f;
  --gold:#f8d590;
  --white:#ffffff;
}
*{margin:0;padding:0;box-sizing:border-box}
html,body{width:1200px;height:922px;overflow:hidden;background:var(--stage)}
body{position:relative;font-family:"Montserrat",sans-serif;font-weight:500;color:var(--white)}
.menu{position:absolute;left:80px;top:54px;width:1027px;height:747px;overflow:hidden;
  background:linear-gradient(100deg,#2c2465 0%,#4e2470 40%,#8a2168 75%,#a02068 100%)}
.plate{position:absolute;border-radius:50%;background:rgba(255,255,255,.04)}
.abs{position:absolute;white-space:nowrap}
.banner{position:absolute;background:var(--cream);color:var(--ink);font-weight:800;
  display:flex;align-items:center;padding-left:12px;
  clip-path:polygon(4% 0,96% 0,100% 50%,96% 100%,4% 100%,0 50%)}
.pill{position:absolute;background:var(--cream);color:var(--ink);font-weight:800;border-radius:20px;
  display:flex;align-items:center;justify-content:center}
.rule{position:absolute;height:2px;background:var(--cream)}
.line{position:absolute;white-space:nowrap;font-size:15.5px;line-height:20px}
.gold{color:var(--gold)}
.brand-blob{position:absolute;left:115px;top:75px}
.brand-name{position:absolute;left:150px;top:160px;width:150px;text-align:center;
  font-weight:800;font-size:28px;line-height:30px;color:var(--orange)}
.photo{position:absolute;border-radius:50%}
.dot{position:absolute;border-radius:50%}
.scheme-title{position:absolute;left:88px;top:812px;font-size:34px;font-weight:600}
.swatch{position:absolute;top:853px;width:45px;height:45px}
</style>
</head>
<body>
<section class="menu">
  <div class="plate" style="left:540px;top:-60px;width:330px;height:330px"></div>
  <div class="plate" style="left:860px;top:40px;width:260px;height:260px"></div>
  <div class="plate" style="left:380px;top:420px;width:260px;height:260px"></div>
  <div class="plate" style="left:-60px;top:380px;width:300px;height:300px"></div>
  <div class="plate" style="left:680px;top:560px;width:320px;height:320px"></div>
</section>

<svg class="brand-blob" width="230" height="230" viewBox="0 0 230 230" aria-hidden="true">
  <path d="M60 20 C100 0 150 30 175 20 C205 10 215 60 210 95 C205 130 225 160 195 190 C165 220 120 200 90 215 C55 230 20 200 20 165 C20 130 5 110 10 80 C15 50 30 35 60 20 Z" fill="#fff"/>
  <path d="M185 10 C200 20 190 40 205 55 C215 70 210 85 200 80" stroke="#fff" stroke-width="8" fill="none" stroke-linecap="round"/>
</svg>
<div class="brand-name">Tadka<br>Lane</div>

<div class="dot" style="left:133px;top:66px;width:14px;height:14px;border:3px solid var(--orange)"></div>
<div class="dot" style="left:336px;top:173px;width:20px;height:20px;background:var(--orange)"></div>
<div class="dot" style="left:340px;top:220px;width:11px;height:11px;border:2px solid var(--orange)"></div>
<div class="dot" style="left:79px;top:237px;width:12px;height:12px;border:2px solid var(--orange)"></div>
<div class="dot" style="left:258px;top:290px;width:12px;height:12px;background:var(--orange)"></div>
<div class="dot" style="left:117px;top:262px;width:11px;height:11px;background:#fff"></div>

<div class="photo" role="img" aria-label="Bowl of chicken curry with onion and paratha" style="left:272px;top:268px;width:128px;height:118px;background:radial-gradient(circle at 45% 45%,#5a3323 0%,#3a2a2a 40%,#e8e4e0 62%,#c9b8a8 100%)"></div>

<div class="banner" style="left:387px;top:69px;width:260px;height:44px;font-size:22px">Build Your Own Meal</div>
<div class="rule" style="left:647px;top:89px;width:344px"></div>
<div class="pill" style="left:989px;top:77px;width:81px;height:26px;font-size:22px">$8.00</div>

<div class="line gold" style="left:398px;top:121px">1.Pick Bowl/Wrap</div>
<div class="line" style="left:412px;top:145px">(Salad Bowl, Basmati Rice Bowl, Curry Rice Bowl, Paratha Wrap)</div>
<div class="line gold" style="left:398px;top:179px">2.Pick Main Curry Option</div>
<div class="line" style="left:413px;top:204px">(Veg Korma, Chana Masala, CTM, Chili Chicken, Tandoori Chicken, Beef Curry +$1,</div>
<div class="line" style="left:413px;top:228px">Goat Curry $2) Double Protein $2 *(For premium curry extra)</div>
<div class="line gold" style="left:398px;top:254px">3.Pick Toppings</div>
<div class="line" style="left:413px;top:278px">(Beets Thoran, Green Beans Thoran, Cabbage Thoran, Chick Pea Salad, Cucumber</div>
<div class="line" style="left:413px;top:303px">Salad, diced Onion, chopped bell pepper, shredded Cheese, cilantro, jalapeno)</div>
<div class="line gold" style="left:398px;top:324px">4.Pick Sauces</div>
<div class="line" style="left:413px;top:348px">Original Mint, Sweet Tamarind, Cool Yogurt, Mango Chilli, Tikka Masala</div>

<div class="banner" style="left:105px;top:397px;width:220px;height:36px;font-size:19px">Lassi/ Indian Shakes</div>
<div class="line" style="left:313px;top:447px">Size</div>
<div class="line" style="left:325px;top:474px">S</div>
<div class="line" style="left:400px;top:474px">L</div>
<div class="line gold" style="left:110px;top:503px">Original Lassi</div><div class="line" style="left:324px;top:503px">2</div><div class="line" style="left:400px;top:503px">2.5</div>
<div class="line gold" style="left:110px;top:523px">Mango Lassi</div><div class="line" style="left:324px;top:523px">2.5</div><div class="line" style="left:400px;top:523px">3</div>
<div class="line gold" style="left:110px;top:543px">Rose Lassi</div><div class="line" style="left:324px;top:543px">2.5</div><div class="line" style="left:400px;top:543px">3</div>
<div class="line gold" style="left:110px;top:564px">Chai Spice Lassi</div><div class="line" style="left:324px;top:564px">2.75</div><div class="line" style="left:400px;top:564px">3.25</div>
<div class="line gold" style="left:110px;top:584px">Cookies N Cream Lassi</div><div class="line" style="left:324px;top:584px">2.75</div><div class="line" style="left:400px;top:584px">3.25</div>
<div class="line gold" style="left:110px;top:604px">Chocolate Hazelnut Lassi</div><div class="line" style="left:324px;top:604px">2.75</div><div class="line" style="left:400px;top:604px">3.25</div>

<div class="banner" style="left:105px;top:640px;width:220px;height:36px;font-size:21px;padding-left:16px">Snacks</div>
<div class="photo" role="img" aria-label="Samosas with green chutney" style="left:365px;top:623px;width:70px;height:64px;background:radial-gradient(circle at 50% 50%,#d9a65a 0%,#b88440 45%,#f2f2f0 70%,#ddd 100%)"></div>
<div class="line gold" style="left:119px;top:692px">Samosa</div><div class="line" style="left:204px;top:692px">$1</div>
<div class="line gold" style="left:282px;top:692px">Sweet Puffs</div><div class="line" style="left:398px;top:692px">$1.49</div>
<div class="line gold" style="left:119px;top:715px">Veg Puffs</div><div class="line" style="left:204px;top:715px">$1.49</div>
<div class="line gold" style="left:282px;top:715px">Beef Puffs</div><div class="line" style="left:398px;top:715px">$1.49</div>
<div class="line gold" style="left:119px;top:738px">Egg Puffs</div><div class="line" style="left:204px;top:738px">$2.49</div>
<div class="line gold" style="left:282px;top:738px">Chicken Puffs</div><div class="line" style="left:398px;top:738px">$1.49</div>

<div class="banner" style="left:477px;top:401px;width:219px;height:36px;font-size:17.5px;padding-left:14px">Chicken Biriyani Bowl</div>
<div class="rule" style="left:696px;top:418px;width:28px"></div>
<div class="pill" style="left:723px;top:407px;width:46px;height:24px;font-size:19px">$7</div>
<div class="line" style="left:495px;top:451px">“The Original <span class="gold">Indian</span> Rice Bowl!</div>
<div class="line" style="left:495px;top:475px">Chicken and rice which has been</div>
<div class="line" style="left:495px;top:500px">baked to perfection.”</div>
<div class="line gold" style="left:495px;top:524px">Served with yogurt sauce, pickle and</div>
<div class="line gold" style="left:495px;top:549px">pappadom.</div>
<div class="photo" role="img" aria-label="Chicken biriyani in a foil bowl" style="left:680px;top:548px;width:100px;height:94px;background:radial-gradient(circle at 50% 45%,#d4a03a 0%,#b8862e 45%,#eeeeee 68%,#cfcfcf 100%)"></div>

<div class="banner" style="left:487px;top:640px;width:221px;height:36px;font-size:23px;padding-left:15px">Chicken Meals</div>
<div class="line gold" style="left:487px;top:692px">Tandoori Chicken /Fries</div><div class="line" style="left:708px;top:692px">$7</div>
<div class="line gold" style="left:487px;top:716px">Chicken Tender/ Fries</div><div class="line" style="left:708px;top:716px">$7</div>
<div class="line gold" style="left:487px;top:741px">Spicy Chicken Tender/ Fries</div><div class="line" style="left:708px;top:741px">$7</div>

<div class="banner" style="left:808px;top:397px;width:220px;height:36px;font-size:20px;padding-left:21px">Loaded Fries</div>
<div class="pill" style="left:1033px;top:403px;width:48px;height:25px;font-size:20px">$6</div>
<div class="line" style="left:823px;top:445px">Chili Chicken Fries</div>
<div class="line" style="left:823px;top:468px">Tandoori Fries</div>
<div class="line" style="left:823px;top:491px">Chicken Tikka Fries</div>

<div class="banner" style="left:807px;top:515px;width:221px;height:37px;font-size:20px;padding-left:20px">Drinks</div>
<div class="line" style="left:823px;top:560px">Iced Tea 32oz</div><div class="line" style="left:982px;top:560px">2</div>
<div class="line" style="left:823px;top:582px">Lemonade 32oz</div><div class="line" style="left:982px;top:582px">2</div>
<div class="line" style="left:823px;top:604px">Masala Tea</div><div class="line" style="left:982px;top:604px">2</div>
<div class="line" style="left:823px;top:625px">Indian Coffee</div><div class="line" style="left:982px;top:625px">2</div>
<div class="line" style="left:823px;top:647px">Soda Can</div><div class="line" style="left:982px;top:647px">1</div>
<div class="line" style="left:823px;top:669px">Water Bottle</div><div class="line" style="left:982px;top:669px">1</div>

<div class="banner" style="left:804px;top:696px;width:221px;height:36px;font-size:21px;padding-left:18px">Dessert</div>
<div class="line" style="left:821px;top:736px">Mango Pudding</div><div class="line" style="left:965px;top:736px">3.50</div>
<div class="line" style="left:821px;top:757px">Rice Pudding</div><div class="line" style="left:965px;top:757px">3.50</div>

<div class="scheme-title">color scheme</div>
<div class="swatch" style="left:86px;background:var(--navy)"></div>
<div class="swatch" style="left:149px;background:var(--red)"></div>
<div class="swatch" style="left:212px;background:var(--magenta)"></div>
<div class="swatch" style="left:274px;background:var(--orange)"></div>
<div class="swatch" style="left:337px;background:var(--cream)"></div>
</body>
</html>
```